PIETRO business card - High end Italian floors and coverings

We need a new design for our business card. We are an exclusive company located in Mexico.
Our commercial name is PIETRO. Our legal name is Grande Volta SA de CV.
We bring the latest trends in materials for floors and walls such as natural stones, wood, leather, design porcelanato tiles and so.
Our company image colors are black, white and red.
Our customers are high end architects and designers.
We are looking for an elegant but fresh design which reflects exclusivity, simplicity and reliability.
(we are working also in a new website)

Requirements
Nice to have
• back and front design
Space for 2 addresses (one for each showroom location)

```html
<!DOCTYPE html>
<html lang="en">
<head>
<meta charset="utf-8">
<title>PIETRO – Locations Card</title>
<link rel="stylesheet" href="https://fonts.googleapis.com/css2?family=Oswald:wght@500;600&family=Questrial&display=swap">
<style>
  :root {
    --ink-dark: #0b0d0e;
    --stone-dark: #1c2022;
    --stone-mid: #2a2f31;
    --brand-red: #d40f14;
    --line-red: #8e0b0e;
    --strip-gray: #6f7578;
    --room-light: #eef2f2;
    --room-mid: #cfd8d8;
    --room-shade: #aeb8b9;
    --text-light: #f4f4f4;
    --text-dark: #1a1a1a;
    --bar-gray: #7d8285;
  }
  html, body { margin: 0; padding: 0; overflow: hidden; background: #ffffff; }
  .card {
    position: relative;
    width: 1200px;
    height: 693px;
    overflow: hidden;
    background: var(--room-light);
  }
  .stone-wall {
    position: absolute; left: 0; top: 0; width: 1200px; height: 370px;
    background: radial-gradient(ellipse at 50% 30%, var(--stone-mid) 0%, var(--stone-dark) 45%, var(--ink-dark) 100%);
  }
  .red-rule {
    position: absolute; left: 0; top: 370px; width: 1200px; height: 7px;
    background: var(--line-red);
  }
  .gray-strip {
    position: absolute; left: 0; top: 379px; width: 1200px; height: 11px;
    background: var(--strip-gray);
  }
  .interior-scene {
    position: absolute; left: 0; top: 390px; width: 1200px; height: 303px;
    background: linear-gradient(180deg, var(--room-mid) 0%, var(--room-light) 35%, #dfe5e5 60%, var(--room-shade) 78%, var(--room-light) 100%);
  }
  .web-address {
    position: absolute; right: 70px; top: 74px; margin: 0;
    font-family: "Questrial", sans-serif; font-size: 31px;
    letter-spacing: 0.5em; color: var(--brand-red);
  }
  .address {
    position: absolute; top: 204px; margin: 0;
    font-family: "Oswald", sans-serif; font-weight: 500;
    font-size: 30px; line-height: 46px; text-transform: uppercase;
    color: var(--text-light); font-style: normal;
  }
  .address--gdl { left: 111px; }
  .address--mex { right: 82px; text-align: right; }
  .phones {
    position: absolute; margin: 0;
    font-family: "Questrial", sans-serif; font-size: 27px;
    letter-spacing: 0.04em;
    line-height: 46px; color: var(--text-dark);
  }
  .phones--gdl { left: 96px; top: 416px; }
  .phones--mex { left: 771px; top: 416px; }
  .phones small { font-size: 14px; letter-spacing: 0.02em; }
  .bar { position: absolute; background: var(--bar-gray); }
  .bar--left { left: 0; top: 588px; width: 45px; height: 29px; }
  .bar--right { left: 303px; top: 588px; width: 94px; height: 29px; }
  .locations-title {
    position: absolute; left: 65px; top: 568px; margin: 0;
    font-family: "Oswald", sans-serif; font-weight: 600;
    font-size: 58px; line-height: 76px; text-transform: uppercase;
    color: var(--brand-red);
    transform: scaleX(0.88); transform-origin: left center;
  }
  .brand-name {
    position: absolute; right: 80px; top: 508px; margin: 0;
    font-family: "Questrial", sans-serif; font-size: 86px; line-height: 86px;
    letter-spacing: 0.05em; color: var(--brand-red);
  }
  .brand-tagline {
    position: absolute; right: 80px; top: 600px; margin: 0;
    font-family: "Questrial", sans-serif; font-size: 23px; line-height: 30px;
    color: var(--text-dark);
  }
</style>
</head>
<body>
  <div class="card">
    <div class="stone-wall" role="img" aria-label="Dark natural stone block wall texture"></div>
    <div class="red-rule"></div>
    <div class="gray-strip" role="img" aria-label="Gray decorative dashed strip"></div>
    <div class="interior-scene" role="img" aria-label="Soft-toned photograph of a modern living room interior with sofas and coffee table"></div>

    <p class="web-address">www.pietro.com.mx</p>

    <address class="address address--gdl">Cristal 1850 Col. Arboledas<br>Guadalajara, Jalisco</address>
    <address class="address address--mex">Lago Coral 245 B<br>Col. Roma, Del. Benito Juarez Mexico&nbsp; D.F.</address>

    <p class="phones phones--gdl">Tel: (33) 3520 4718 <small>(Guadalajara)</small><br>Cell: (33) 1847 2093</p>
    <p class="phones phones--mex">Tel: (55) 5284 6031 <small>(Mexico)</small></p>

    <div class="bar bar--left"></div>
    <div class="bar bar--right"></div>
    <h2 class="locations-title">Locations</h2>

    <p class="brand-name">PIETRO</p>
    <p class="brand-tagline">italian floors &amp; coverings</p>
  </div>
</body>
</html>
```